Marlow Yardcraft need a flyer - A6 - Double sided

We need a flyer that will engage potential customer in need for gardening services. We offer high quality gardening services spanning from lawn mowing and weeding to soil improvement to tree pruning and so on.
I would like a double sided flyer A6 size. I trust your expert touch in terms of lay out but the general idea I had was to have one side with the logo, a catchy picture (or more), the website/phone number/address and on the flip side a little more text focusing on the client perspective with statement such as 'Let us do the hard work so that you can enjoy your garden' (obviously the wording isn't my strongest skill) but the idea is to get into the customer perspective;
I would also like to list all the service we can offer such as but not limited to weeding, pruning, lawn care, green waste disposal, soil improvement, hedging, edging, lawn mowing,...
Happy for you to use any picture free of right from the internet if necessary

Target Market(s)

Home owner & Businesses

Industry/Entity Type

Landscape Gardening

Requirements
Must have
• website - http://yardcraft-marlow.com.au (feel free to browse the website to get ideas on color theme and overall look)
• phone number - (08) 6341 2705
Nice to have
• a list of services on offer
• phone number and website
• being customer perspective focused (the benefits for the customer) - perhaps on the flip side some text like 'highly trained and experienced landscape gardeners so that the job is done perfectly every time', 'always carrying all range of commercial grade tools so that we can tackle any job', 'Experienced gardeners so that the job is achieve faster' (it doesn't have to be in those exact words as I trust that you may be expert in wording as well as designers?)

```html
<!DOCTYPE html>
<html lang="en">
<head>
<meta charset="utf-8">
<title>Marlow Yardcraft – Reliable Affordable Gardening</title>
<link href="https://fonts.googleapis.com/css2?family=Montserrat:wght@700;800&family=Open+Sans:wght@400;600&display=swap" rel="stylesheet">
<style>
  :root {
    --green: #8cc63f;
    --green-dark: #6fa52a;
    --charcoal: #3a3d40;
    --paper: #ffffff;
    --mist: #eef0ee;
    --ink: #3d4044;
  }
  * { box-sizing: border-box; margin: 0; padding: 0; }
  html, body { width: 807px; height: 1200px; overflow: hidden; background: var(--paper); }
  .flyer { position: relative; width: 807px; height: 1200px; overflow: hidden; background: var(--paper); font-family: "Open Sans", sans-serif; color: var(--ink); }

  .photo { position: absolute; top: 0; height: 500px; }
  .photo--gardener { left: 0; width: 403px; background: linear-gradient(160deg, #6f9a3c 0%, #3f6a22 45%, #a9c86a 100%); }
  .photo--mower { left: 404px; width: 403px; background: linear-gradient(200deg, #cfd3d6 0%, #8a8f94 35%, #c9302c 60%, #4f7d2b 100%); }

  .roof { position: absolute; left: 0; top: 0; width: 807px; height: 560px; }

  .brand { position: absolute; top: 378px; left: 0; width: 807px; text-align: center; font-family: "Montserrat", sans-serif; font-weight: 800; font-size: 44px; line-height: 1.05; letter-spacing: 1px; text-transform: uppercase; color: var(--charcoal); }
  .brand span { display: block; }

  .headline { position: absolute; top: 545px; left: 0; width: 807px; height: 240px; background: var(--charcoal); text-align: center; padding-top: 26px; }
  .headline__kicker { font-family: "Montserrat", sans-serif; font-weight: 800; font-size: 44px; line-height: 1.2; color: var(--green); letter-spacing: 2px; text-transform: uppercase; }
  .headline__main { font-family: "Open Sans", sans-serif; font-weight: 400; font-size: 108px; line-height: 1.1; color: var(--paper); letter-spacing: 3px; text-transform: uppercase; }

  .services-tag { position: absolute; top: 798px; left: 0; height: 48px; width: 270px; background: var(--green); clip-path: polygon(0 0, 92% 0, 100% 100%, 0 100%); color: var(--paper); font-family: "Montserrat", sans-serif; font-weight: 800; font-size: 28px; letter-spacing: 2px; line-height: 48px; padding-left: 40px; }
  .services-rule { position: absolute; top: 842px; left: 0; width: 807px; height: 4px; background: var(--green); }

  .services { position: absolute; top: 868px; left: 0; width: 807px; display: flex; padding: 0 30px 0 50px; }
  .services ul { list-style: none; }
  .services ul:first-child { width: 330px; }
  .services li { font-size: 21px; line-height: 31px; color: var(--ink); position: relative; padding-left: 22px; white-space: nowrap; }
  .services li::before { content: ""; position: absolute; left: 0; top: 11px; width: 9px; height: 9px; border-radius: 50%; background: var(--green); }

  .contact { position: absolute; bottom: 0; left: 0; width: 807px; height: 90px; background: var(--mist); border-top: 5px solid var(--green); border-bottom: 10px solid var(--green); display: flex; align-items: center; justify-content: center; gap: 60px; font-family: "Open Sans", sans-serif; font-weight: 600; font-size: 26px; color: var(--ink); }
  .contact__item { display: flex; align-items: center; gap: 14px; }
  .contact__item svg { width: 28px; height: 28px; fill: var(--green-dark); }
</style>
</head>
<body>
<main class="flyer">
  <div class="photo photo--gardener" role="img" aria-label="Gardener in high-visibility shirt pruning a leafy tree"></div>
  <div class="photo photo--mower" role="img" aria-label="Close-up of a red lawn mower on green grass"></div>

  <svg class="roof" viewBox="0 0 807 560" aria-hidden="true">
    <polygon points="0,470 403,290 807,470 807,560 0,560" fill="var(--charcoal)"/>
    <polygon points="0,498 403,320 807,498 807,560 0,560" fill="var(--paper)"/>
    <polyline points="0,485 403,305 807,485" fill="none" stroke="var(--green)" stroke-width="4"/>
  </svg>

  <div class="brand"><span>Marlow</span><span>Yardcraft</span></div>

  <section class="headline">
    <p class="headline__kicker">Reliable Affordable</p>
    <h1 class="headline__main">Gardening</h1>
  </section>

  <div class="services-rule"></div>
  <div class="services-tag">SERVICES</div>

  <div class="services">
    <ul>
      <li>Lawn Care</li>
      <li>Tree Pruning in Perth</li>
      <li>Hedge Trimming</li>
      <li>Organic Gardening</li>
      <li>Mulching</li>
    </ul>
    <ul>
      <li>Weed Control</li>
      <li>Rubbish and Green Waste Removal</li>
      <li>Fertilising &amp; Soil Improvement</li>
      <li>Perth Garden Edging and Kerbing</li>
      <li>Perth Garden Beds</li>
      <li>Garden Clean Up Perth</li>
    </ul>
  </div>

  <footer class="contact">
    <div class="contact__item">
      <svg viewBox="0 0 24 24" aria-hidden="true"><path d="M6.6 10.8a15.1 15.1 0 0 0 6.6 6.6l2.2-2.2a1 1 0 0 1 1-.25 11.4 11.4 0 0 0 3.6.57 1 1 0 0 1 1 1V20a1 1 0 0 1-1 1A17 17 0 0 1 3 4a1 1 0 0 1 1-1h3.5a1 1 0 0 1 1 1c0 1.25.2 2.45.57 3.57a1 1 0 0 1-.25 1z"/></svg>
      <span>(08) 6341 2705</span>
    </div>
    <div class="contact__item">
      <svg viewBox="0 0 24 24" aria-hidden="true"><path d="M12 2a10 10 0 1 0 0 20 10 10 0 0 0 0-20zm6.9 6h-2.9a15.6 15.6 0 0 0-1.4-3.6A8 8 0 0 1 18.9 8zM12 4c.8 1.2 1.5 2.5 1.9 4h-3.8c.4-1.5 1.1-2.8 1.9-4zM4.3 14a8 8 0 0 1 0-4h3.4a16.5 16.5 0 0 0 0 4zm.8 2h2.9c.3 1.3.8 2.5 1.4 3.6A8 8 0 0 1 5.1 16zM8 8H5.1a8 8 0 0 1 4.3-3.6C8.8 5.5 8.3 6.7 8 8zm4 12c-.8-1.2-1.5-2.5-1.9-4h3.8c-.4 1.5-1.1 2.8-1.9 4zm2.3-6H9.7a14.7 14.7 0 0 1 0-4h4.6a14.7 14.7 0 0 1 0 4zm.3 5.6c.6-1.1 1.1-2.300 1.4-3.6h2.9a8 8 0 0 1-4.3 3.6zm1.7-5.6a16.5 16.5 0 0 0 0-4h3.4a8 8 0 0 1 0 4z"/></svg>
      <span>www.yardcraft-marlow.com.au</span>
    </div>
  </footer>
</main>
</body>
</html>
```